Maplecrest geriatric care need flyer design

Flyer design to introduce physician working with maplecrest geriatric care.
the flyer can be simple but need to be catchy.
A sample attached just mainly for reference purpose.
The format must be editable with ms word.

thank you

```html
<!DOCTYPE html>
<html lang="en">
<head>
<meta charset="utf-8">
<title>Maplecrest Geriatric Care – Physician Introduction Flyer</title>
<link rel="stylesheet" href="https://fonts.googleapis.com/css2?family=Open+Sans:ital,wght@0,400;0,600;0,700;1,600&display=swap">
<style>
  :root {
    --red: #d3222a;
    --red-dark: #b71c22;
    --red-light: #e8464c;
    --blush: #f6e6e3;
    --ink: #333333;
    --muted: #555555;
    --blue: #2a4f9a;
    --paper: #ffffff;
    --backdrop: #e9e9e9;
    --avatar: #d4d4d4;
  }
  * { box-sizing: border-box; margin: 0; padding: 0; }
  html, body {
    width: 1200px; height: 796px; overflow: hidden;
    background: var(--backdrop);
    font-family: "Open Sans", Arial, sans-serif;
    color: var(--ink);
  }
  .flyer {
    position: absolute; left: 325px; top: 10px;
    width: 549px; height: 776px;
    background: var(--paper);
    box-shadow: 0 4px 18px rgba(0,0,0,.18);
    overflow: hidden;
    display: flex; flex-direction: column;
  }
  .hero {
    position: relative; flex: none; height: 160px;
    background: linear-gradient(90deg, #e8e2dc 0%, #f1ece7 35%, #f7f5f2 60%, #ffffff 80%);
  }
  .hero-photo {
    position: absolute; left: 0; top: 0; width: 360px; height: 160px;
    background: radial-gradient(ellipse at 35% 55%, #e9d4c6 0%, #e4ddd6 45%, rgba(240,236,232,0) 80%);
  }
  .brand {
    position: absolute; right: 24px; top: 34px;
    display: flex; align-items: center; gap: 8px;
  }
  .brand-dot { width: 18px; height: 18px; border-radius: 50%; background: var(--red); }
  .brand-name { font-size: 19px; font-weight: 700; color: var(--red); letter-spacing: -.2px; }
  .intro-band {
    flex: none;
    background: var(--red);
    border-top: 5px solid var(--red-light);
    color: #fff; text-align: center;
    font-size: 10px; font-style: italic; font-weight: 600; line-height: 1.45;
    padding: 6px 20px 7px;
  }
  .profile { flex: none; display: flex; gap: 18px; padding: 14px 28px 4px; }
  .avatar {
    flex: none; width: 70px; height: 62px; background: var(--avatar);
    display: flex; align-items: flex-end; justify-content: center;
  }
  .doctor-name { font-size: 14px; font-weight: 700; line-height: 1.3; margin-top: 2px; }
  .doctor-role { font-size: 11.5px; font-weight: 600; color: var(--blue); }
  .body-text { flex: none; padding: 6px 28px 0; font-size: 10.5px; line-height: 1.5; color: var(--muted); }
  .body-text p { margin-bottom: 6px; text-align: center; }
  .interests {
    flex: none;
    background: var(--blush);
    margin-top: 2px; padding: 8px 28px 10px;
  }
  .interests h2 {
    font-size: 14px; font-weight: 400; color: var(--red); line-height: 1.3; margin-bottom: 4px;
    text-align: center;
  }
  .interests ul { list-style: none; font-size: 10.5px; line-height: 1.6; color: var(--ink); }
  .interests li::before { content: "\2022"; margin-right: 12px; }
  .more { flex: none; padding: 10px 28px 12px; font-size: 10.5px; line-height: 1.55; color: var(--muted); }
  .more p { text-align: center; }
  .more strong { color: var(--ink); }
  .hl { color: var(--red); font-weight: 700; }
  .contact {
    flex: 1;
    background: var(--red);
    border-top: 4px solid var(--red-dark);
    color: #fff; padding: 20px 28px 16px;
    display: grid; grid-template-columns: 160px 1fr; grid-template-rows: auto 1fr;
    column-gap: 28px; row-gap: 8px;
  }
  .contact h3 {
    font-size: 15px; font-weight: 600; letter-spacing: .3px; white-space: nowrap;
    padding-bottom: 6px; border-bottom: 1.5px solid #fff; margin-bottom: 10px;
  }
  .contact .lead { font-size: 11.5px; line-height: 1.4; }
  .contact .address { font-size: 11.5px; line-height: 1.4; padding-top: 22px; white-space: nowrap; }
  .contact .address b { font-weight: 700; display: block; }
  .contact .lines {
    grid-column: 2; grid-row: 2; justify-self: end; align-self: start;
    font-size: 11.5px; line-height: 1.45; white-space: nowrap;
  }
  .contact .lines b { font-weight: 700; }
</style>
</head>
<body>
<article class="flyer">
  <header class="hero">
    <div class="hero-photo" role="img" aria-label="Photo of a smiling senior couple"></div>
    <div class="brand">
      <span class="brand-dot"></span>
      <span class="brand-name">Maplecrest Geriatric Care</span>
    </div>
  </header>

  <div class="intro-band">Maplecrest geriatric care consist of a group of geriatricians specialised in providing medical consultation for patient above 65 years old in both community and permanent residential care.</div>

  <section class="profile">
    <div class="avatar">
      <svg width="46" height="50" viewBox="0 0 46 50" aria-hidden="true">
        <circle cx="23" cy="16" r="11" fill="#a9a9a9"/>
        <path d="M2 50 C2 34 12 29 23 29 C34 29 44 34 44 50 Z" fill="#a9a9a9"/>
      </svg>
    </div>
    <div>
      <div class="doctor-name">Dr. XYT<br>MBBS (Kingsford), FRACP, Clin Dip Pall med.</div>
      <div class="doctor-role">Consultant Geriatrician and Physician</div>
    </div>
  </section>

  <section class="body-text">
    <p>We are very pleased to introduce you to Consultant Geriatrician and Physician who has commenced consulting at Ashgrove Private Hospital and is available to see patients who are 65 years and over.</p>
    <p>Completed his specialist training with Riverside Health in 2012 and then undertook 6 months of diploma training in palliative care medicine prior to commencing as a consultant geriatrician.</p>
  </section>

  <section class="interests">
    <h2>He has an interest in all geriatric related problems with special interest in:</h2>
    <ul>
      <li>Comprehensive geriatric assessment (over 65 years)</li>
      <li>Memory assessment</li>
      <li>Fall and balance assessment</li>
      <li>Polypharmacy</li>
    </ul>
  </section>

  <section class="more">
    <p>He is also available to visit residential care facilities, should you require any advice.<br>
    <strong>Other languages spoken:</strong> Mandarin, Cantonese and Malay<br>
    Daniel can be contacted on <span class="hl">0400 555 218</span> for patient advice.<br>
    Alternatively, you can fax you referral especially for residents in residential care facilities to <span class="hl">(03) 9000 4127</span>.</p>
  </section>

  <footer class="contact">
    <div>
      <h3>CONTACT DETAILS</h3>
      <p class="lead">For all appointment and enquiries, please contact:</p>
    </div>
    <div class="address">
      <b>Address:</b>
      Suite 4.10, Larkfield Medical Centre<br>
      Fernvale, 22-24 Sample Street<br>
      Fernvale VIC 3000
    </div>
    <div class="lines">
      <b>Tel:</b> (03)<br>
      <b>Fax:</b> (03) 9000 4127<br>
      <b>Email:</b> info@maplecrestgc.com.au<br>
      <b>Website:</b> www.maplecrestgc.com.au
    </div>
  </footer>
</article>
</body>
</html>
```